Letterhead and business card design

We have recently had a logo designed by brightnook. now we need a corporate identity with business card and lettehead design.

Target Market(s)

law firms corporates

Industry/Entity Type

Business

Requirements
Should not have
• cheesy detecive stuff like magnifying glasses etxcc

```html
<!DOCTYPE html>
<html lang="en">
<head>
<meta charset="utf-8">
<title>Halvorsen &amp; Marsh — Stationery</title>
<link href="https://fonts.googleapis.com/css2?family=Cormorant+Garamond:wght@500&family=Open+Sans:wght@400;600&display=swap" rel="stylesheet">
<style>
  :root{
    --bg:#eeeeee;
    --paper:#ffffff;
    --ink:#5a5c5c;
    --ink-soft:#8a8c8c;
    --silver-light:#a9abab;
    --silver-dark:#7b7d7d;
    --rule:#c9cbcb;
    --sign:#3a6fb0;
  }
  *{box-sizing:border-box;margin:0;padding:0}
  html,body{width:1200px;height:859px;overflow:hidden;background:var(--bg)}
  .canvas{position:relative;width:1200px;height:859px}
  .sheet{position:absolute;background:var(--paper);box-shadow:0 2px 8px rgba(0,0,0,.12);overflow:hidden}
  .silver{background:linear-gradient(135deg,var(--silver-light),var(--silver-dark))}

  .brand{font-family:'Cormorant Garamond',serif;font-weight:500;color:var(--ink);white-space:nowrap;line-height:1}
  .tagline{font-family:'Open Sans',sans-serif;font-weight:400;text-transform:uppercase;letter-spacing:.18em;color:var(--ink-soft);white-space:nowrap;line-height:1.3}
  .on-silver .brand,.on-silver .tagline{color:#fff}
  .small{font-family:'Open Sans',sans-serif;color:var(--ink-soft)}

  /* Letterhead */
  .letterhead{left:40px;top:40px;width:420px;height:594px;padding:36px 40px}
  .letterhead .masthead{text-align:right}
  .letterhead .brand{font-size:24px}
  .letterhead .tagline{font-size:6.5px;margin-top:5px}
  .letter{margin-top:48px;font-family:'Open Sans',sans-serif;font-size:8.5px;line-height:1.65;color:var(--ink)}
  .letter p{margin-bottom:10px}
  .letter .salutation{font-weight:600}
  .signoff{margin-top:28px;text-align:right;font-size:8.5px}
  .signoff strong{font-weight:600}
  .signature{display:block;margin:6px 0 4px auto}
  .letter-footer{position:absolute;left:40px;right:40px;bottom:28px;border-top:1px solid var(--rule);padding-top:8px;font-size:7px;text-align:center}

  /* Folder */
  .folder{left:490px;top:40px;width:420px;height:594px}
  .folder .spine{position:absolute;left:14px;top:0;bottom:0;width:1px;background:rgba(255,255,255,.35)}
  .folder .masthead{position:absolute;right:40px;top:90px;text-align:center}
  .folder .brand{font-size:32px}
  .folder .tagline{font-size:8.5px;margin-top:8px}
  .folder .web{position:absolute;left:40px;bottom:34px;font-family:'Open Sans',sans-serif;font-size:10px;color:#fff;letter-spacing:.05em}

  /* Business cards */
  .card{width:230px;height:131px}
  .card-front{left:940px;top:40px;padding:16px 18px}
  .card-front .brand{font-size:15px}
  .card-front .tagline{font-size:5px;margin-top:3px}
  .card-front .person{margin-top:16px;font-family:'Open Sans',sans-serif;font-size:8px;font-weight:600;color:var(--ink)}
  .card-front .role{font-size:6.5px}
  .card-front .contact{margin-top:8px;font-size:6px;line-height:1.5}
  .card-back{left:940px;top:196px;padding:18px;display:flex;flex-direction:column;justify-content:center;align-items:center}
  .card-back .brand{font-size:17px}
  .card-back .tagline{font-size:5.5px;margin-top:4px}
  .card-back .web{margin-top:20px;font-size:6.5px;color:#fff;letter-spacing:.05em}

  /* Envelopes */
  .envelope{width:360px;height:180px;top:660px}
  .envelope-front{left:40px;padding:22px 26px}
  .envelope-front .brand{font-size:20px}
  .envelope-front .tagline{font-size:6px;margin-top:4px}
  .envelope-front .address{margin-top:10px;font-size:6.5px}
  .envelope-front .band{position:absolute;left:0;right:0;bottom:0;height:10px}
  .envelope-back{left:440px}
  .envelope-back .flap{position:absolute;left:0;right:0;top:0;height:58px;display:flex;flex-direction:column;justify-content:center;align-items:center}
  .envelope-back .brand{font-size:16px}
  .envelope-back .tagline{font-size:5.5px;margin-top:3px}
  .envelope-back .return{position:absolute;left:20px;right:20px;top:72px;font-size:6px}
</style>
</head>
<body>
<main class="canvas">

  <article class="sheet letterhead">
    <header class="masthead">
      <div class="brand">Halvorsen &amp; Marsh</div>
      <div class="tagline">Private Inquiry and Risk Advisory</div>
    </header>
    <section class="letter">
      <p class="salutation">Dear Sir / Madam</p>
      <p>Thank you for contacting our office regarding your recent enquiry. We have reviewed the matter and prepared a summary of our findings for your records.</p>
      <p>Our team will remain available to discuss the next steps at a time that suits you. Please contact us directly with any questions.</p>
      <p>We appreciate your trust and look forward to working with you.</p>
      <div class="signoff">
        Yours faithfully, <strong>HALVORSEN AND MARSH</strong>
        <svg class="signature" width="90" height="26" viewBox="0 0 90 26"><path d="M4 18 C20 4 34 24 46 14 S70 10 86 16" fill="none" stroke="var(--sign)" stroke-width="1.2"/></svg>
        Aaron Lindqvist<br>Director
      </div>
    </section>
    <footer class="letter-footer small">Tel +64 9 555 0142 · Fax +64 9 555 0143 · PO Box 118, Harbour Lane, Wellington, New Zealand</footer>
  </article>

  <article class="sheet folder silver on-silver">
    <span class="spine"></span>
    <header class="masthead">
      <div class="brand">Halvorsen &amp; Marsh</div>
      <div class="tagline">Private Inquiry and Risk Advisory</div>
    </header>
    <div class="web">www.thecaseworks.co.nz</div>
  </article>

  <article class="sheet card card-front">
    <div class="brand">Halvorsen &amp; Marsh</div>
    <div class="tagline">Private Inquiry and Risk Advisory</div>
    <div class="person">Aaron Lindqvist</div>
    <div class="role small">Director</div>
    <div class="contact small">M +64 21 555 0178 · E aaron@thecaseworks.co.nz<br>PO Box 118, Harbour Lane, Wellington</div>
  </article>

  <article class="sheet card card-back silver on-silver">
    <div class="brand">Halvorsen &amp; Marsh</div>
    <div class="tagline">Private Inquiry and Risk Advisory</div>
    <div class="web small">www.thecaseworks.co.nz</div>
  </article>

  <article class="sheet envelope envelope-front">
    <div class="brand">Halvorsen &amp; Marsh</div>
    <div class="tagline">Private Inquiry and Risk Advisory</div>
    <div class="address small">PO Box 118, Harbour Lane, Wellington, New Zealand</div>
    <span class="band silver"></span>
  </article>

  <article class="sheet envelope envelope-back">
    <div class="flap silver on-silver">
      <div class="brand">Halvorsen &amp; Marsh</div>
      <div class="tagline">Private Inquiry and Risk Advisory</div>
    </div>
    <div class="return small">If undelivered please return to PO Box 118, Harbour Lane, Wellington, New Zealand</div>
  </article>

</main>
</body>
</html>
```